Marketplace App for Gamers needs Brand Identity

You are competing to produce the Brand Identity for Pelorin, a new marketplace app for iOS and Android. Pelorin is specific to the gaming industry, providing a platform for gaming enthusiasts to buy, sell and trade PC and console games as well as gaming hardware.

This project requires production of a logo, single-page marketing website and user interface design for the mobile application. All outputs should be as PSD files so they can be easily included into the mobile application by our developers.

The successful design will communicate modernity, edginess and and a sense of belonging to the gaming community. Attached is a logo we are fond of (but not attached to). It is a fusion of a hawk and micro chip. The text font is ideal.

Desired colours are shades of greens, blues or purples. Gray may be included with any of these three but we are not keen to mix green with purple.

About Us

Pelorin is being developer by Varnel Holdings. Our focus is on building mobile first e-commerce applications with millennials and other digital natives in mind.

Industry/Entity Type

Industry

Number of Pages Required

1 page

Font styles to use
Sans Serif

Colors
3276b5
33b8a4
886aae

```html
<!DOCTYPE html>
<html lang="en">
<head>
<meta charset="utf-8">
<title>Pelorin – Home Screen</title>
<link href="https://fonts.googleapis.com/css2?family=Open+Sans:wght@300;400;600;700&display=swap" rel="stylesheet">
<style>
  :root {
    --teal: #33b8a4;
    --blue: #3276b5;
    --purple: #886aae;
    --ink: #ffffff;
    --ink-soft: rgba(255,255,255,0.85);
    --stage: #f4f4f4;
    --screen-dark: #1b1d1f;
    --hero-dark: #2a2c2e;
    --font: "Open Sans", sans-serif;
  }
  * { box-sizing: border-box; margin: 0; padding: 0; }
  html, body {
    width: 1200px; height: 900px; overflow: hidden;
    background: var(--stage);
    font-family: var(--font);
  }
  .app-screen {
    position: absolute; left: 375px; top: 50px;
    width: 450px; height: 800px;
    background: var(--screen-dark);
    overflow: hidden;
    box-shadow: 0 20px 50px rgba(0,0,0,0.18);
  }
  .status-bar {
    height: 24px; background: var(--teal); color: var(--ink);
    font-size: 11px; display: flex; align-items: center;
    justify-content: space-between; padding: 0 8px;
  }
  .status-left, .status-right { display: flex; align-items: center; gap: 5px; width: 140px; }
  .status-right { justify-content: flex-end; }
  .signal { letter-spacing: -1px; font-size: 10px; }
  .battery { width: 22px; height: 10px; border: 1px solid var(--ink); border-radius: 2px; padding: 1px; }
  .battery span { display: block; width: 22%; height: 100%; background: var(--ink); }
  .nav-bar {
    height: 53px; background: var(--teal); color: var(--ink);
    display: flex; align-items: center; justify-content: center; position: relative;
  }
  .menu-icon { position: absolute; left: 14px; top: 17px; }
  .app-title { font-weight: 700; font-size: 17px; letter-spacing: 1px; }
  .hero {
    position: relative; height: 273px;
    background: linear-gradient(160deg, #3a3c3e 0%, var(--hero-dark) 45%, #151617 100%);
    display: flex; flex-direction: column; align-items: center; justify-content: center;
  }
  .hero-title {
    color: var(--ink); font-weight: 300; font-size: 29px; line-height: 1.2;
    text-align: center; padding: 0 30px; margin-top: -20px;
  }
  .hero-dots { position: absolute; bottom: 14px; display: flex; gap: 6px; }
  .hero-dots i { width: 6px; height: 6px; border-radius: 50%; background: rgba(255,255,255,0.45); }
  .hero-dots i.active { background: var(--ink); }
  .tile-grid { display: grid; grid-template-columns: 225px 225px; grid-template-rows: 225px 225px; }
  .tile {
    position: relative; display: flex; flex-direction: column;
    align-items: center; justify-content: center; color: var(--ink); text-align: center;
  }
  .tile-buy { background: linear-gradient(150deg, #5a4a40 0%, #1f2220 50%, #2f6a2a 100%); }
  .tile-sell { background: linear-gradient(135deg, #3a3a3a 0%, #1c1d1e 55%, #4f7c3a 100%); }
  .tile-trade { background: linear-gradient(150deg, #2a2a2a 0%, #5a1e22 35%, #1b1b1b 100%); }
  .tile-news { background: linear-gradient(140deg, #3b2a5a 0%, #1f3a4a 50%, #2c2140 100%); }
  .tile::before { content: ""; position: absolute; inset: 0; background: rgba(0,0,0,0.25); }
  .tile > * { position: relative; }
  .tile-icon { display: block; height: 36px; margin-bottom: 8px; }
  .tile-label { font-weight: 700; font-size: 22px; letter-spacing: 0.5px; line-height: 1.2; }
  .tile-note { font-size: 10px; text-transform: uppercase; color: var(--ink-soft); margin-top: 2px; }
</style>
</head>
<body>
<main class="app-screen">
  <div class="status-bar">
    <div class="status-left"><span class="signal">●●●○○</span><span>KESTOVA</span>
      <svg width="12" height="9" viewBox="0 0 12 9"><path d="M1 3.5a7 7 0 0 1 10 0M3 5.5a4 4 0 0 1 6 0" stroke="#fff" stroke-width="1.3" fill="none"/><circle cx="6" cy="7.6" r="1.1" fill="#fff"/></svg>
    </div>
    <div class="status-time">4:21 PM</div>
    <div class="status-right">
      <svg width="7" height="11" viewBox="0 0 7 11"><path d="M1 3l5 5-2.5 2.5V0.5L6 3 1 8" stroke="#fff" stroke-width="1" fill="none"/></svg>
      <span>22%</span><div class="battery"><span></span></div>
    </div>
  </div>
  <header class="nav-bar">
    <svg class="menu-icon" width="20" height="16" viewBox="0 0 20 16"><path d="M0 1h20M0 8h20M0 15h20" stroke="#fff" stroke-width="2"/></svg>
    <h1 class="app-title">PELORIN</h1>
  </header>
  <section class="hero" role="img" aria-label="Close-up photo of a gaming motherboard">
    <p class="hero-title">Providing a Platform for Gaming Enthusiasts</p>
    <div class="hero-dots"><i></i><i class="active"></i><i></i></div>
  </section>
  <nav class="tile-grid">
    <a class="tile tile-buy" role="img" aria-label="Photo of a gaming mouse with green light">
      <svg class="tile-icon" width="40" height="36" viewBox="0 0 40 36"><path d="M12 12a8 8 0 0 1 16 0" stroke="#fff" stroke-width="3" fill="none"/><path d="M4 13h32l-4 21H8z" fill="#fff"/><path d="M14 17v13M20 17v13M26 17v13" stroke="#333" stroke-width="2"/></svg>
      <span class="tile-label">BUY</span><span class="tile-note">54 items available</span>
    </a>
    <a class="tile tile-sell" role="img" aria-label="Photo of a console game controller">
      <svg class="tile-icon" width="44" height="36" viewBox="0 -3 44 36"><path d="M10 3h24c6 0 9 8 9 16 0 7-5 10-9 5l-4-5H14l-4 5c-4 5-9 2-9-5C1 11 4 3 10 3z" fill="#fff"/><path d="M8 13h8M12 9v8" stroke="#333" stroke-width="2"/><circle cx="31" cy="10" r="1.8" fill="#333"/><circle cx="35" cy="14" r="1.8" fill="#333"/></svg>
      <span class="tile-label">SELL</span><span class="tile-note">Sell your items now!</span>
    </a>
    <a class="tile tile-trade" role="img" aria-label="Photo of a motherboard with red memory modules">
      <svg class="tile-icon" width="40" height="36" viewBox="0 -1 40 36"><path d="M20 2v28M8 6h24M12 32h16" stroke="#fff" stroke-width="2.5"/><path d="M8 6l-6 12h12zM32 6l-6 12h12z" stroke="#fff" stroke-width="1.8" fill="none"/><path d="M2 18a6 4 0 0 0 12 0zM26 18a6 4 0 0 0 12 0z" fill="#fff"/></svg>
      <span class="tile-label">TRADE</span><span class="tile-note">53 waiting for trades</span>
    </a>
    <a class="tile tile-news" role="img" aria-label="Photo of a crowded esports arena">
      <svg class="tile-icon" width="40" height="36" viewBox="0 0 40 36"><rect x="4" y="2" width="30" height="32" fill="#fff"/><rect x="8" y="6" width="10" height="9" fill="#333"/><path d="M21 7h9M21 11h9M21 15h9M8 20h22M8 24h22M8 28h22" stroke="#333" stroke-width="2"/></svg>
      <span class="tile-label">NEWS</span><span class="tile-note">2 new post</span>
    </a>
  </nav>
</main>
</body>
</html>
```